Business Card Design, including supply of raw art files plus a vector diagram of the zelvon logo and

We need the business card design for a company that is launching a new exciting product. The brief requires the submission of the following once the final design is chosen:

- business card layout including raw files
- a composite vector image file of the zelvon logo and tag line
- a standalone vector image file of the zelvon logo

The product will be launched as a customer engagement app.

It has 4 core modules which enables a person to do multiple things - book tours and activities, order takeaways, search for local deals and offers. A universal currency is at the heart of this product. When you use the app, you earn cashback rewards when shopping or buying at any of the merchant partners across the modules as . These rewards can then be used as full or part payment when buying goods or services at these merchant partners.

The business card must help us build the brand, communicate the benefit of the brand's key focus - the ability to earn and burn this universal cashback ccurrency - across the 4 modules - booking of tours and activities, ordering, searching for local deals and payment.

We would like the design to use the brand's blue colour the hex colour is: 00
Dark grey : 646464
Darker blue shadow: 058bdd
Main Blue: 0084ff

We need to translate this into a CMYK print or spot colour print.

Both print options to be supplied as separate files.

An example of the base concept we have in mind is attached for your reference.

The font used by the brand is Proxima Nova.

Note: the duration has been set as 2 days.

Industry/Entity Type

Business

Contact Information for Business Card

Carla Mendoza
Marketing
W: www.zelvon.example
M: + 61 400555123
T: +61 2 5550 1473
A: Suite 7, Level 2, 14-18 Harwick Street, Sydney, NSW, 2000, Australia

Font styles to use
Sans Serif

Requirements
Must have
• zelVon logo and tagline
• address details
• zelVon icons as supplied
Nice to have
• would like to have the option of a spot varnish layer over the logo and icons at the back of the card

```html
<!DOCTYPE html>
<html lang="en">
<head>
<meta charset="utf-8">
<title>zelVon business card</title>
<link rel="stylesheet" href="https://fonts.googleapis.com/css2?family=Montserrat:wght@300;400;600&display=swap">
<style>
  :root {
    --page: #e6e7e8;
    --card-dark: #464646;
    --brand-blue: #3187cc;
    --brand-blue-light: #429cd8;
    --icon-cyan: #29abe2;
    --ink: #3e3e3e;
    --white: #ffffff;
  }
  * { margin: 0; padding: 0; box-sizing: border-box; }
  html, body { width: 1200px; height: 927px; overflow: hidden; background: var(--page); }
  body { position: relative; font-family: "Montserrat", sans-serif; color: var(--ink); }

  .card { position: absolute; top: 87px; width: 430px; height: 753px; border-radius: 32px; overflow: hidden; }
  .card--front { left: 146px; background: var(--white); }
  .card--back { left: 623px; background: var(--card-dark); }
  .card__art { position: absolute; inset: 0; }

  .brand { position: absolute; left: 44px; top: 203px; }
  .brand__dot { width: 100px; height: 100px; border-radius: 50%; background: var(--brand-blue-light); }
  .brand__name { position: absolute; left: 120px; top: 10px; font-weight: 400; font-size: 64px; line-height: 1; color: var(--ink); white-space: nowrap; }
  .brand__tagline { position: absolute; left: 150px; top: 272px; width: 232px; text-align: right; font-weight: 300; font-size: 17px; color: var(--ink); white-space: nowrap; }

  .person { position: absolute; left: 0; right: 0; top: 345px; text-align: center; }
  .person__name { font-weight: 600; font-size: 28px; line-height: 34px; color: var(--brand-blue); }
  .person__role { font-weight: 400; font-size: 17px; line-height: 22px; }

  .address { position: absolute; left: 0; right: 0; top: 416px; text-align: center; font-size: 17px; line-height: 23px; font-weight: 400; font-style: normal; }

  .contact-icons { position: absolute; left: 164px; top: 470px; }

  .contact { position: absolute; left: 0; right: 0; top: 498px; text-align: center; list-style: none; font-size: 17px; line-height: 23.5px; font-weight: 400; }
  .contact__accent { color: var(--brand-blue); font-weight: 600; }

  .modules { position: absolute; left: 60px; top: 640px; display: flex; gap: 6px; align-items: flex-end; }
  .module { display: flex; flex-direction: column; align-items: center; width: 64px; }
  .module--lead { width: 48px; }
  .module__icon { width: 44px; height: 44px; }
  .module__label { margin-top: 6px; font-size: 6px; line-height: 8px; text-transform: uppercase; white-space: nowrap; height: 8px; }

  .back-mark { position: absolute; left: 99px; top: 260px; width: 230px; height: 230px; border-radius: 50%; background: var(--brand-blue-light); }
</style>
</head>
<body>

<section class="card card--front" aria-label="Front of card">
  <svg class="card__art" width="430" height="753" viewBox="0 0 430 753" aria-hidden="true">
    <path d="M0 0 H430 V209 Q215 40 0 209 Z" fill="var(--card-dark)"/>
    <path d="M0 209 Q215 40 430 209" fill="none" stroke="var(--brand-blue)" stroke-width="4"/>
    <rect x="0" y="722" width="430" height="31" fill="var(--card-dark)"/>
    <rect x="72" y="722" width="286" height="31" fill="var(--white)"/>
    <rect x="78" y="722" width="274" height="31" fill="var(--brand-blue)"/>
  </svg>

  <div class="brand">
    <div class="brand__dot"></div>
    <div class="brand__name">zelVon</div>
  </div>
  <p class="brand__tagline">earn and spend anywhere</p>

  <div class="person">
    <h1 class="person__name">Carla Mendoza</h1>
    <p class="person__role">Marketing</p>
  </div>

  <address class="address">
    Suite 7, Level 2, 14-18 Harwick Street<br>
    Sydney, NSW, 2000, Australia
  </address>

  <svg class="contact-icons" width="102" height="16" viewBox="0 0 102 16" aria-hidden="true" fill="none" stroke="var(--brand-blue)" stroke-width="1.4">
    <rect x="3" y="1" width="8" height="13" rx="1.5"/>
    <path d="M25 2 q-3 1 -1 6 q2 5 5 6 l2 -2 -2.5 -2 -1.5 1 q-2 -2 -2 -4 l1.5 -1 -1 -3 z" fill="var(--brand-blue)" stroke="none"/>
    <rect x="48" y="6" width="13" height="6" fill="var(--brand-blue)" stroke="none"/>
    <rect x="50.5" y="2" width="8" height="4"/>
    <rect x="50.5" y="11" width="8" height="3" fill="var(--white)"/>
    <circle cx="75" cy="8" r="6.2"/>
    <ellipse cx="75" cy="8" rx="2.8" ry="6.2"/>
    <path d="M69 8 H81 M70 5 H80 M70 11 H80"/>
    <rect x="88" y="3" width="13" height="10" rx="1"/>
    <path d="M88 3 L94.5 9 L101 3"/>
  </svg>

  <ul class="contact">
    <li>+ 61 400555123</li>
    <li>+61 2 5550 1473</li>
    <li>+61 2 5550 1482</li>
    <li>www.<span class="contact__accent">zelvon</span>.example</li>
    <li>carla.mendoza@northpeak.example</li>
  </ul>

  <div class="modules">
    <div class="module module--lead">
      <svg class="module__icon" viewBox="0 0 44 44" aria-hidden="true">
        <path d="M4 8 q6 -6 14 -2 l-2 3 8 -1 -3 -7 -2 3 q-10 -4 -16 3 z" fill="var(--brand-blue)"/>
        <circle cx="22" cy="22" r="11" fill="var(--brand-blue)"/>
        <text x="22" y="28" text-anchor="middle" font-family="Montserrat, sans-serif" font-weight="600" font-size="16" fill="var(--white)">$</text>
        <path d="M40 36 q-6 6 -14 2 l2 -3 -8 1 3 7 2 -3 q10 4 16 -3 z" fill="var(--brand-blue)"/>
      </svg>
      <span class="module__label"></span>
    </div>
    <div class="module">
      <svg class="module__icon" viewBox="0 0 44 44" aria-hidden="true"><rect x="1" y="0" width="42" height="42" fill="var(--icon-cyan)"/></svg>
      <span class="module__label">Cashback rewards</span>
    </div>
    <div class="module">
      <svg class="module__icon" viewBox="0 0 56 44" style="width:56px" aria-hidden="true">
        <rect x="1" y="8" width="54" height="34" rx="4" fill="var(--icon-cyan)"/>
        <rect x="18" y="2" width="20" height="8" rx="2" fill="var(--icon-cyan)"/>
        <circle cx="28" cy="25" r="12" fill="var(--white)"/>
        <circle cx="28" cy="25" r="8.5" fill="var(--icon-cyan)"/>
        <circle cx="28" cy="25" r="6" fill="var(--white)"/>
      </svg>
      <span class="module__label">Tours&amp;Activities</span>
    </div>
    <div class="module">
      <svg class="module__icon" viewBox="0 0 44 44" aria-hidden="true" stroke="var(--icon-cyan)" stroke-width="2.4" fill="none">
        <path d="M12 2 V12 q0 4 4 5 M16 2 V12 M20 2 V12 q0 4 -4 5"/>
        <path d="M16 17 L36 43"/>
        <ellipse cx="35" cy="8" rx="5" ry="7" transform="rotate(35 35 8)" fill="var(--icon-cyan)"/>
        <path d="M31 14 L8 43"/>
      </svg>
      <span class="module__label">Mobile ordering</span>
    </div>
    <div class="module">
      <svg class="module__icon" viewBox="0 0 44 44" aria-hidden="true"><rect x="1" y="0" width="42" height="42" fill="var(--icon-cyan)"/></svg>
      <span class="module__label">Local offers</span>
    </div>
  </div>
</section>

<section class="card card--back" aria-label="Back of card">
  <div class="back-mark"></div>
</section>

</body>
</html>
```